Membership card Design

Hi I need a new membership card design for a social University club located in New Zealand. Our club name is called Maple Lantern Circle (MLCIR) and we provide a social hub for international students from Asia to meet local students. We are a non-profit organization that organizes activities such as paintball, ski trips, parties and day trips for our members. We need designs that look more like a membership card than a name card because we will be giving them to our members as a proof of membership. We would prefer a design that is simple in the front and with our club details, contacts and a place to write down a membership number on the back. We would like our card to have designs using the colours red, black, grey and orange. The design must incoporate the logo attached in this project. If possible, we would like the flower in the Hong Kong Flag to be incoporated in the design. The final design must look more like a membership card than a name card and communicate professionalism and high quality.
Updates

Target Market(s)

University Students

Industry/Entity Type

Non-Profit

Requirements
Must have
• The design must include:

The logo of our club
Our facebook page details: www.friendspage.example/maplelantern.cir
Our email: maplelanterncir@mailbox.example
A place behind the card to print membership numbers.

```html
<!DOCTYPE html>
<html lang="en">
<head>
<meta charset="utf-8">
<title>Maple Lantern Circle — Membership Card</title>
<link rel="stylesheet" href="https://fonts.googleapis.com/css2?family=Cinzel:wght@600&family=Crimson+Text:wght@400&display=swap">
<style>
  :root {
    --backdrop: #f2f2f2;
    --card-red: #d0111c;
    --card-red-deep: #9a0710;
    --card-red-light: #e8262f;
    --band-light: #fbfbfb;
    --band-mid: #e4e4e4;
    --band-edge: #c9c9c9;
    --brand-red: #d3141e;
    --gold: #f6c445;
    --slot-light: #f4f4f4;
    --slot-dark: #bdbdbd;
  }
  * { box-sizing: border-box; margin: 0; padding: 0; }
  html, body {
    width: 1200px;
    height: 787px;
    overflow: hidden;
    background: var(--backdrop);
  }
  .canvas {
    position: relative;
    width: 1200px;
    height: 787px;
    display: flex;
    align-items: center;
    justify-content: space-evenly;
  }
  .card {
    position: relative;
    width: 520px;
    height: 310px;
    border-radius: 22px;
    overflow: hidden;
    box-shadow: 0 10px 24px rgba(0, 0, 0, 0.22);
  }
  .card-pattern {
    position: absolute;
    inset: 0;
    background: radial-gradient(ellipse at 50% 40%, var(--card-red-light) 0%, var(--card-red) 55%, var(--card-red-deep) 100%);
  }
  .front-band {
    position: absolute;
    left: 0;
    right: 0;
    top: 68px;
    height: 168px;
    background: linear-gradient(180deg, var(--band-light) 0%, var(--band-mid) 70%, var(--band-edge) 100%);
    box-shadow: 0 2px 6px rgba(0, 0, 0, 0.25), 0 -2px 6px rgba(0, 0, 0, 0.2);
    display: flex;
    align-items: center;
    justify-content: center;
    gap: 14px;
  }
  .brand-mark {
    width: 40px;
    height: 40px;
    border-radius: 50%;
    background: var(--brand-red);
  }
  .brand-name {
    font-family: "Cinzel", serif;
    font-weight: 600;
    font-size: 31px;
    color: var(--brand-red);
    letter-spacing: 0.5px;
  }
  .back-contacts {
    position: absolute;
    top: 58px;
    left: 0;
    right: 0;
    text-align: center;
    font-family: "Crimson Text", serif;
    font-size: 16px;
    line-height: 1.55;
    color: var(--gold);
  }
  .member-number {
    position: absolute;
    left: 68px;
    top: 146px;
    display: flex;
    align-items: center;
    gap: 12px;
  }
  .member-number-label {
    font-family: "Crimson Text", serif;
    font-size: 24px;
    color: var(--gold);
  }
  .member-number-slot {
    width: 290px;
    height: 40px;
    background: linear-gradient(90deg, var(--slot-dark) 0%, var(--slot-light) 30%, var(--slot-light) 70%, var(--slot-dark) 100%);
    box-shadow: inset 0 1px 3px rgba(0, 0, 0, 0.35);
  }
  .back-brand {
    position: absolute;
    right: 22px;
    bottom: 22px;
    display: flex;
    align-items: center;
    gap: 7px;
  }
  .back-brand .brand-mark {
    width: 18px;
    height: 18px;
    background: var(--gold);
  }
  .back-brand .brand-name {
    font-size: 14px;
    color: var(--gold);
  }
</style>
</head>
<body>
<main class="canvas">
  <section class="card card-front">
    <div class="card-pattern" role="img" aria-label="Red background with a faint repeating bauhinia flower pattern"></div>
    <div class="front-band">
      <span class="brand-mark"></span>
      <span class="brand-name">Maple Lantern Circle</span>
    </div>
  </section>

  <section class="card card-back">
    <div class="card-pattern" role="img" aria-label="Red background with a faint repeating bauhinia flower pattern"></div>
    <p class="back-contacts">
      www.friendspage.example/maplelantern.cir<br>
      maplelanterncir@mailbox.example
    </p>
    <div class="member-number">
      <span class="member-number-label">#</span>
      <span class="member-number-slot"></span>
    </div>
    <div class="back-brand">
      <span class="brand-mark"></span>
      <span class="brand-name">Maple Lantern Circle</span>
    </div>
  </section>
</main>
</body>
</html>
```